Wordpress website design for a high-end painting business

We are currently rebranding and are looking to update our Wordpress theme. We have recently rebranded our logo on PixelHarbor, and would like our website to be equally as refined.
Our business is named “Kestrel Painters”. We are a high-end painting business that is known for being professional and having high standards. Our clean and professional image is important as it separates us from our competition. Our current website can be found at www.wrenfieldcoatings.co.nz . We designed the site ourselves so it is understandably rudimentary. We are generally happy with the. page layout of our existing site, but we like a professional remodel. Any ideas on improvement welcomed.
We would like the front page of the website to summarise all of the info throughout the whole website (I.e introduction, photos, testimonials, contact info etc.) as visitors typically scroll through the first page to see that we are reputable and get to our contact number/email contact at the bottom of the page. We would like this first page to give a clean well rounded image of our business. We would like the gallery to be a scroll through of large photos, as it is difficult to see paint details in smaller photos. A contact page with an enquiry section would also be good.
For the colour scheme, we would like something that fits a bold, masculine and high end theme (similar to our logo attached).
We would like the footer to include Veltora paint logos and the accredited painter logo we have included as these are important to our profession.
We have attached some photos of our work also. I will add more in the coming days. More can also be found on our website.
If you have questions or comments, please don’t hesitate to ask and I will get back as soon as possible.
We are open to your own interpretation or ideas for a better layout/site provided they fit the general brief of being a well rounded site for our profession.
Thanks,
Kestrel Painters.
Target Market(s)
High end clients
Industry/Entity Type
Painting (interior and exterior)
Coding
Coded - Design and coding required
Requirements
Must have
- Classy feel, separating us from typical painting companies. Well rounded homepage.
Nice to have
- Lots of examples of our work
Should not have
- Untidy paint motifs (eg, paint droplets, paint splashes)

```html
<!DOCTYPE html>
<html lang="en">
<head>
<meta charset="utf-8">
<title>Kestrel Painters – Home</title>
<link href="https://fonts.googleapis.com/css2?family=Playfair+Display:wght@700;800&family=Poppins:wght@400;500&display=swap" rel="stylesheet">
<style>
:root{
  --navy:#1b2330;
  --gold:#8b6b45;
  --gold-light:#a88560;
  --ink:#2a2a2a;
  --white:#ffffff;
  --serif:'Playfair Display', Georgia, serif;
  --sans:'Poppins', Arial, sans-serif;
}
*{box-sizing:border-box;margin:0;padding:0}
html,body{width:1200px;height:3631px;overflow:hidden}
body{position:relative;background:var(--white);font-family:var(--sans);color:var(--ink)}
.abs{position:absolute}
.circle-btn{position:absolute;width:37px;height:37px;border-radius:50%;display:flex;align-items:center;justify-content:center}
.circle-btn.navy{background:var(--navy)}
.circle-btn.gold{background:var(--gold)}
.circle-btn.white{background:var(--white)}
.pill{position:absolute;border-radius:20px;display:flex;align-items:center;justify-content:center;gap:8px;font-size:13px;font-weight:500;letter-spacing:.3px}
.pill.navy{background:var(--navy);color:var(--white)}
.pill.gold{background:var(--gold);color:var(--white)}
.pill.white{background:var(--white);color:var(--navy)}

/* header */
.site-header{position:absolute;top:0;left:0;width:1200px;height:106px;background:var(--white);z-index:3}
.brand{position:absolute;left:110px;top:-25px;width:172px;height:177px;border-radius:50%;background:var(--white);z-index:4;display:flex;align-items:flex-end;justify-content:center;padding-bottom:40px}
.brand-name{font-family:var(--sans);font-weight:500;color:var(--navy);font-size:15px;letter-spacing:.3px}
.main-nav a{position:absolute;top:45px;font-size:13px;color:var(--navy);text-decoration:none;font-weight:500;letter-spacing:.3px}
.main-nav a.active{color:var(--gold)}
.nav-mark{position:absolute;left:365px;top:0;width:38px;height:3px;background:var(--gold)}
.nav-mark.bottom{top:103px}

/* hero */
.hero{position:absolute;top:106px;left:0;width:1200px;height:503px;background:linear-gradient(180deg,#5b6470 0%,#7d7362 45%,#5f6a45 80%,#4d5a38 100%)}
.hero::after{content:"";position:absolute;inset:0;background:rgba(20,24,32,.35)}
.hero h1{position:absolute;top:140px;left:0;width:1200px;text-align:center;font-family:var(--serif);font-weight:700;color:var(--white);font-size:64px;line-height:74px;z-index:1}

/* about */
.about-photo{position:absolute;left:145px;top:761px;width:410px;height:410px;border-radius:50%;background:linear-gradient(180deg,#aab7c2 0%,#d8d3c4 45%,#6f8e4a 80%,#5c7a3c 100%);box-shadow:0 0 0 10px #f1efec}
.section-title{font-family:var(--serif);font-weight:800;font-size:56px;color:var(--navy)}
.section-title span{color:var(--gold)}
.about-text{position:absolute;left:610px;top:810px;width:470px;font-size:13.5px;line-height:21px;color:#333}
.about-text p{margin-bottom:21px}
.about-text a{color:var(--gold)}

/* services */
.services-band{position:absolute;top:1290px;left:0;width:1200px;height:315px;background:linear-gradient(180deg,#222a38 0%,#2c3545 60%,#1e2633 100%)}
.card{position:absolute;width:302px;height:302px;border:2px solid #fff}
.card-label{position:absolute;left:16px;bottom:20px;font-family:var(--serif);font-weight:700;font-size:22px;color:#fff}
.card-arrow{position:absolute;right:16px;bottom:26px}

/* testimonials */
.testimonials{position:absolute;top:1906px;left:0;width:1200px;height:628px;background:linear-gradient(135deg,#2a2f36 0%,#1c2027 55%,#24282e 100%)}
.testi-title{position:absolute;left:0;width:588px;top:2250px;text-align:center;font-family:var(--serif);font-weight:800;font-size:48px;color:var(--gold)}
.quote{position:absolute;left:482px;width:598px;padding:36px 46px 0 23px;color:#fff;font-size:13.5px;line-height:21px}
.quote.navy{top:1981px;height:226px;background:var(--navy)}
.quote.gold{top:2214px;height:244px;background:var(--gold)}
.quote .mark{font-family:var(--serif);font-weight:800;font-size:48px;line-height:30px;height:34px}
.quote cite{display:block;font-style:normal;font-size:12.5px;margin-top:10px}

/* footer */
.site-footer{position:absolute;top:3151px;left:0;width:1200px;height:480px;background:linear-gradient(180deg,#1a1d22 0%,#15181d 100%)}
.foot-brand{position:absolute;left:120px;top:3400px;width:210px;text-align:center;font-family:var(--sans);font-weight:500;font-size:22px;color:var(--gold-light)}
.foot-h{position:absolute;font-family:var(--serif);font-weight:700;font-size:17px;color:#fff}
.foot-t{position:absolute;font-size:14px;color:#fff;line-height:18px}
.foot-t.gold{color:var(--gold-light)}
.field{position:absolute;background:#4a4f57;border-radius:14px;color:#9aa0a8;font-size:11px;padding:9px 14px}
.social{position:absolute;width:37px;height:37px;border-radius:50%;background:#fff}
.foot-links a{position:absolute;top:3596px;font-size:13px;color:#fff;text-decoration:none}
</style>
</head>
<body>

<header class="site-header">
  <nav class="main-nav">
    <span class="nav-mark"></span><span class="nav-mark bottom"></span>
    <a class="active" style="left:367px">HOME</a>
    <a style="left:441px">ABOUT US</a>
    <a style="left:544px">SERVICES</a>
    <a style="left:642px">GALLERY</a>
    <a style="left:735px">TESTIMONIALS</a>
  </nav>
  <a class="pill navy" style="left:863px;top:35px;width:127px;height:37px">CONTACT
    <svg width="14" height="10" viewBox="0 0 14 10"><path d="M0 5h12M8 1l4 4-4 4" stroke="#fff" stroke-width="1.4" fill="none"/></svg></a>
  <span class="circle-btn navy" style="left:997px;top:35px"><svg width="14" height="11" viewBox="0 0 14 11"><rect x=".7" y=".7" width="12.6" height="9.6" rx="1" stroke="#fff" fill="none" stroke-width="1.2"/><path d="M1 1l6 5 6-5" stroke="#fff" fill="none" stroke-width="1.2"/></svg></span>
  <span class="circle-btn gold" style="left:1043px;top:35px"><svg width="14" height="14" viewBox="0 0 14 14"><path d="M3 1l2 3-1.5 1.5a8 8 0 0 0 5 5L10 9l3 2-1.5 2.5C6 13 1 8 .5 2.5z" stroke="#fff" fill="none" stroke-width="1.1"/></svg></span>
</header>
<div class="brand"><span class="brand-name">Kestrel Painters</span></div>

<section class="hero" role="img" aria-label="Photo of a large two-storey painted house with gardens">
  <h1>World Famous Painting<br>Agency.</h1>
  <a class="pill white" style="left:526px;top:313px;width:148px;height:37px;z-index:1">CONTACT US
    <svg width="14" height="10" viewBox="0 0 14 10"><path d="M0 5h12M8 1l4 4-4 4" stroke="#1b2330" stroke-width="1.4" fill="none"/></svg></a>
  <span class="circle-btn white" style="left:468px;top:448px;z-index:1"><svg width="14" height="10" viewBox="0 0 14 10"><path d="M14 5H2M6 1L2 5l4 4" stroke="#1b2330" stroke-width="1.4" fill="none"/></svg></span>
  <span class="circle-btn gold" style="left:695px;top:448px;z-index:1"><svg width="14" height="10" viewBox="0 0 14 10"><path d="M0 5h12M8 1l4 4-4 4" stroke="#fff" stroke-width="1.4" fill="none"/></svg></span>
</section>

<section class="about">
  <div class="about-photo" role="img" aria-label="Photo of a freshly painted single-storey home"></div>
  <h2 class="section-title abs" style="left:610px;top:720px">About <span>Us</span></h2>
  <div class="about-text">
    <p>Here at Kestrel Painters, we take a lot of pride in our work. We strive to ensure the highest quality paint-work, paying close attention to detail to provide a long lasting finish. Our clients are always our priority, we aim to deliver beyond their expectations. It is our goal to provide an excellent service from start to finish through clear communication, free quoting and transparency with our pricing.</p>
    <p>We take great pride in the preparation of surfaces for painting and only use the best quality products to ensure we achieve the best finish for you. Our qualified interior designer can also assist you with your colour selection as a part of our free colour consultancy service.</p>
    <p>If you are looking at painting your property, or have any questions, please don't hesitate to call Rohan on <a>021 555 0193</a>.</p>
  </div>
  <a class="pill gold" style="left:610px;top:1138px;width:136px;height:36px">ABOUT US
    <svg width="14" height="10" viewBox="0 0 14 10"><path d="M0 5h12M8 1l4 4-4 4" stroke="#fff" stroke-width="1.4" fill="none"/></svg></a>
</section>

<section class="services">
  <div class="services-band" role="img" aria-label="Darkened photo of a house exterior"></div>
  <h2 class="section-title abs" style="left:120px;top:1350px;color:#fff">Our <span>Services</span></h2>
  <div class="card" role="img" aria-label="Exterior painting: two-storey house with lawn" style="left:121px;top:1452px;background:linear-gradient(180deg,#9fb3c6 0%,#d7d9d4 45%,#5d8a3a 75%,#6c9a40 100%)"></div>
  <div class="card" style="left:448px;top:1452px;background:linear-gradient(180deg,#3c3f45 0%,#55575a 60%,#34363a 100%)">
    <div role="img" aria-label="Interior painting: freshly painted living room" style="position:absolute;inset:0"></div>
    <span class="card-label">Interior Painting</span>
    <svg class="card-arrow" width="22" height="14" viewBox="0 0 22 14"><path d="M0 7h20M14 1l6 6-6 6" stroke="#fff" stroke-width="1.8" fill="none"/></svg>
  </div>
  <div class="card" role="img" aria-label="Wallpaper feature wall in a bathroom" style="left:776px;top:1452px;background:linear-gradient(90deg,#6a6e66 0%,#7b7f77 70%,#dfe4e6 72%,#cfd6da 100%)"></div>
  <span class="circle-btn navy" style="left:491px;top:1794px"><svg width="14" height="10" viewBox="0 0 14 10"><path d="M14 5H2M6 1L2 5l4 4" stroke="#fff" stroke-width="1.4" fill="none"/></svg></span>
  <a class="pill navy" style="left:546px;top:1794px;width:132px;height:37px">VIEW ALL
    <svg width="14" height="10" viewBox="0 0 14 10"><path d="M0 5h12M8 1l4 4-4 4" stroke="#fff" stroke-width="1.4" fill="none"/></svg></a>
  <span class="circle-btn gold" style="left:695px;top:1794px"><svg width="14" height="10" viewBox="0 0 14 10"><path d="M0 5h12M8 1l4 4-4 4" stroke="#fff" stroke-width="1.4" fill="none"/></svg></span>
</section>

<section class="testimonials-wrap">
  <div class="testimonials" role="img" aria-label="Darkened photo of a painted weatherboard home"></div>
  <h2 class="testi-title">Testimonials</h2>
  <span class="circle-btn navy" style="left:175px;top:2334px"><svg width="14" height="10" viewBox="0 0 14 10"><path d="M14 5H2M6 1L2 5l4 4" stroke="#fff" stroke-width="1.4" fill="none"/></svg></span>
  <a class="pill navy" style="left:228px;top:2334px;width:132px;height:37px">VIEW ALL
    <svg width="14" height="10" viewBox="0 0 14 10"><path d="M0 5h12M8 1l4 4-4 4" stroke="#fff" stroke-width="1.4" fill="none"/></svg></a>
  <span class="circle-btn gold" style="left:377px;top:2334px"><svg width="14" height="10" viewBox="0 0 14 10"><path d="M0 5h12M8 1l4 4-4 4" stroke="#fff" stroke-width="1.4" fill="none"/></svg></span>
  <blockquote class="quote navy">
    <div class="mark">“</div>
    These guys are great from beginning to end. Very professional, excellent businessmen, hard workers, and top-quality work. Excellent communication, do what they say they will do and more, and really go the extra mile to make the job as painless as possible. Without reservations would highly recommend!
    <cite>— &nbsp;Martin Hale (2020)</cite>
  </blockquote>
  <blockquote class="quote gold">
    <div class="mark">“</div>
    Daniel and his Team have done an amazing job painting our house. Without a doubt hiring them was our best decision. Attention to detail, great communication, respect towards our needs, working within the budget are just a few things to describe them. I will be recommending Kestrel Painters and Decorators for many years to come. Thank you, Guys!
    <cite>— &nbsp;Helena Marsh (2019)</cite>
  </blockquote>
</section>

<section class="gallery">
  <h2 class="section-title abs" style="left:0;width:1200px;text-align:center;top:2595px">Our <span>Gallery</span></h2>
  <div class="card" role="img" aria-label="Gallery: painted two-storey house exterior" style="left:121px;top:2693px;height:300px;border:none;background:linear-gradient(180deg,#9fb3c6 0%,#d7d9d4 45%,#5d8a3a 75%,#6c9a40 100%)"></div>
  <div class="card" role="img" aria-label="Gallery: painted lounge with wall lights" style="left:448px;top:2693px;height:300px;border:none;background:linear-gradient(180deg,#d9d3c8 0%,#b8ab99 55%,#8f8275 100%)"></div>
  <div class="card" role="img" aria-label="Gallery: wallpaper feature wall in a bathroom" style="left:776px;top:2693px;height:300px;border:none;background:linear-gradient(90deg,#6a6e66 0%,#7b7f77 70%,#dfe4e6 72%,#cfd6da 100%)"></div>
  <span class="circle-btn navy" style="left:480px;top:3040px"><svg width="14" height="10" viewBox="0 0 14 10"><path d="M14 5H2M6 1L2 5l4 4" stroke="#fff" stroke-width="1.4" fill="none"/></svg></span>
  <a class="pill navy" style="left:533px;top:3040px;width:134px;height:37px">VIEW ALL
    <svg width="14" height="10" viewBox="0 0 14 10"><path d="M0 5h12M8 1l4 4-4 4" stroke="#fff" stroke-width="1.4" fill="none"/></svg></a>
  <span class="circle-btn gold" style="left:683px;top:3040px"><svg width="14" height="10" viewBox="0 0 14 10"><path d="M0 5h12M8 1l4 4-4 4" stroke="#fff" stroke-width="1.4" fill="none"/></svg></span>
</section>

<footer class="site-footer-wrap">
  <div class="site-footer" role="img" aria-label="Darkened photo of a house at dusk"></div>
  <div class="foot-brand">Kestrel Painters</div>

  <h3 class="foot-h" style="left:450px;top:3207px">Contact Us</h3>
  <p class="foot-t gold" style="left:450px;top:3246px;font-size:17px">Call: 021 555 0193</p>
  <p class="foot-t" style="left:450px;top:3268px">hello@kestrelpainters.co.nz</p>
  <p class="foot-t gold" style="left:450px;top:3306px;font-size:12px">ADDRESS:</p>
  <p class="foot-t" style="left:450px;top:3323px;font-size:13.5px">Lorem ipsum work 195 N-4646<br>work design - 1234</p>
  <p class="foot-t gold" style="left:450px;top:3398px;font-size:12px">FOLLOW US</p>
  <span class="social" style="left:450px;top:3423px"></span>
  <span class="social" style="left:495px;top:3423px"></span>
  <span class="social" style="left:540px;top:3423px"></span>

  <h3 class="foot-h" style="left:742px;top:3207px">Send Us Message</h3>
  <div class="field" style="left:742px;top:3247px;width:162px;height:33px">Name</div>
  <div class="field" style="left:918px;top:3247px;width:162px;height:33px">Phone</div>
  <div class="field" style="left:742px;top:3294px;width:338px;height:32px">Email</div>
  <div class="field" style="left:742px;top:3339px;width:338px;height:68px">Message</div>
  <a class="pill gold" style="left:742px;top:3422px;width:135px;height:31px">Submit
    <svg width="14" height="10" viewBox="0 0 14 10"><path d="M0 5h12M8 1l4 4-4 4" stroke="#fff" stroke-width="1.4" fill="none"/></svg></a>

  <span class="abs" style="left:390px;top:3501px;width:113px;height:38px;background:#1d2f74" aria-label="Veltora partner badge"></span>
  <span class="abs" style="left:527px;top:3501px;width:284px;height:38px;background:#1aa0d8" aria-label="Accredited painter badge"></span>

  <span class="abs" style="left:1093px;top:3538px;width:44px;height:44px;border-radius:50%;background:var(--gold);box-shadow:0 0 0 4px rgba(255,255,255,.25);display:flex;align-items:center;justify-content:center">
    <svg width="12" height="14" viewBox="0 0 12 14"><path d="M6 14V2M1 6l5-5 5 5" stroke="#fff" stroke-width="1.6" fill="none"/></svg></span>

  <span class="abs" style="left:120px;top:3580px;width:960px;height:1px;background:rgba(255,255,255,.15)"></span>
  <p class="foot-t" style="left:120px;top:3596px;font-size:12.5px">© 2022 <span style="color:var(--gold-light)">KESTREL PAINTERS</span> All Right Reserved</p>
  <nav class="foot-links">
    <a style="left:630px;color:var(--gold-light);text-decoration:underline">Home</a>
    <a style="left:711px">About Us</a>
    <a style="left:811px">Services</a>
    <a style="left:909px">Testimonials</a>
    <a style="left:1034px">Gallery</a>
  </nav>
</footer>

</body>
</html>
```